Website/Logo Design

We need a logo and website design for an opinion mining startup called VantaLume. Our technology mines the web to automatically discover what people are saying about brands, products, etc. The project we are fielding here is for our informational, public-facing website. In its initial incarnation, it will simply be a vehicle for marketing materials and information on our company and its offerings, but it should be flexible enough to expand as more content/functionality is added.

Some designs we like are:
http://www.tradewhisk.example
http://www.gorvantel.example
http://www.kfz.example
http://www.lintwharf.example
http://moxbarrel.example
http://trundlemq.example
http://www.zopla.example
Updates

All, please try to shy away from using a photo of a person as the focal point of the design.  Our company is more technological than social.

Target Market(s)

Primarily businesses interested in sentiment analysis (typically companies involved in advertising, market research, PR, etc.)

Industry/Entity Type

It Company

Requirements
Must have
• We are looking for a clean, modern, and professional design. This includes a logo, homepage, and internal page if it will differ from the homepage.
Nice to have
• It would be excellent if you could provide an HTML mockup if your design is chosen.
Should not have
• Flash, excessive bells and whistles

```html
<!DOCTYPE html>
<html lang="en">
<head>
<meta charset="utf-8">
<title>VantaLume</title>
<link rel="stylesheet" href="https://fonts.googleapis.com/css2?family=Jost:wght@400;500&family=Noto+Sans:wght@400;700&display=swap">
<style>
:root{
  --backdrop:#9aa2ab;
  --backdrop-light:#aab2ba;
  --page:#ffffff;
  --nav:#1c5fa6;
  --nav-dark:#124a86;
  --brand-deep:#0c437f;
  --brand:#1a68b4;
  --brand-bright:#2a86dc;
  --aqua:#35d6e8;
  --sidebar:#ececec;
  --ink:#1d1d1d;
  --heading:#1b64a8;
  --rule:#9a9a9a;
}
*{box-sizing:border-box;margin:0;padding:0}
html,body{width:1129px;height:1200px;overflow:hidden;background:var(--backdrop)}
.stage{position:absolute;left:0;top:0;width:1263px;height:1343px;transform:scale(.8939);transform-origin:0 0;
  background:linear-gradient(180deg,var(--backdrop-light),var(--backdrop));
  font-family:"Noto Sans",Verdana,sans-serif;color:var(--ink)}
.page{position:absolute;left:130px;top:8px;width:1003px;height:1290px;background:var(--page);
  border-radius:0 0 14px 14px;box-shadow:0 2px 8px rgba(0,0,0,.35);overflow:hidden}
.abs{position:absolute}
h1,h2,h4{font-weight:400}
.nav-bar{left:0;top:0;width:1003px;height:47px;background:linear-gradient(180deg,var(--nav),var(--nav-dark))}
.nav{left:390px;top:16px;display:flex;font-family:"Jost",sans-serif;font-size:14.5px;color:#fff;letter-spacing:.3px}
.nav span{white-space:nowrap}
.nav .sep{margin:0 24px;opacity:.9}
.aqua-strip{left:5px;top:52px;width:55px;height:330px;background:linear-gradient(90deg,#b5f6ff,var(--aqua) 40%,#1e9fcf)}
.hero{left:340px;top:52px;width:658px;height:390px;
  background:radial-gradient(ellipse 70% 55% at 40% 35%,#d6f0fc 0%,#5fb0e4 28%,#1a6cb6 60%,#0b3f78 100%)}
.logo-column{left:60px;top:0;width:280px;height:380px;background:linear-gradient(180deg,#1a64ad,var(--brand-deep));
  color:#fff;font-family:"Jost",sans-serif;text-align:center}
.logo-column .name{margin-top:148px;font-size:44px;font-weight:400;letter-spacing:1px}
.hero-marks{left:672px;top:56px;font-family:"Jost",sans-serif;font-size:72px;line-height:1;color:#fff;letter-spacing:2px}
.tagline{left:421px;top:306px;font-family:"Jost",sans-serif;font-size:23px;line-height:28px;color:#111;
  text-shadow:-1px -1px 0 #fff,1px -1px 0 #fff,-1px 1px 0 #fff,1px 1px 0 #fff}
.wave{left:0;top:340px}
.call{left:774px;top:470px;font-family:"Jost",sans-serif;font-size:18px;line-height:23px;color:#fff}
.call-icon{left:872px;top:437px}
.sidebar{left:60px;top:560px;width:280px;height:740px;background:var(--sidebar)}
.panel{position:absolute;border:3px solid var(--brand-bright);border-radius:8px}
.panel-title{font-family:"Jost",sans-serif;font-size:18px;text-align:center}
.search{left:83px;top:447px;width:234px;height:85px;background:linear-gradient(180deg,#2670b8,#134c8a)}
.search .panel-title{color:#fff;margin-top:9px}
.field{background:#fff;border:1px solid #8aa;height:30px}
.search .field{position:absolute;left:13px;top:38px;width:206px}
.cases{left:83px;top:572px;width:232px;height:228px;background:#f7f7f7;border-color:var(--brand)}
.cases .panel-title{color:var(--heading);margin-top:11px}
.cases h4{font-family:"Jost",sans-serif;font-size:15px;color:var(--heading);margin:20px 0 0 11px}
.cases p{font-size:11px;line-height:13.4px;margin:6px 10px 0 11px;letter-spacing:.45px}
.more{font-weight:700;font-size:11px;text-align:right;letter-spacing:.4px}
.cases .more{margin:12px 16px 0 0}
.contact{left:83px;top:837px;width:234px;height:380px;background:linear-gradient(180deg,#1c5fa2,#1a63ab)}
.contact .panel-title{color:#fff;margin-top:10px}
.contact label{position:absolute;left:15px;color:#fff;font-size:11px;font-weight:700;letter-spacing:.5px}
.contact .field{position:absolute;left:12px;width:206px}
.btn{position:absolute;top:342px;width:76px;height:26px;background:linear-gradient(180deg,#fff,#dfe6ee);
  border:1px solid #5a7fa8;border-radius:5px;color:var(--nav);font-size:12px;font-weight:700;text-align:center;line-height:24px}
.main-title{left:372px;top:563px;font-family:"Jost",sans-serif;font-size:24px;color:var(--heading);letter-spacing:.3px}
.copy{font-size:12px;line-height:14.5px;letter-spacing:.25px}
.intro{left:372px;top:626px;width:420px}
.body-text{left:372px;top:770px;width:596px}
.photo{border:2px solid var(--brand)}
.team{left:797px;top:627px;width:180px;height:128px;background:linear-gradient(180deg,#e7e7e7,#bfc3c6 45%,#2a2d33)}
.blog-title{left:372px;top:922px;font-family:"Jost",sans-serif;font-size:17px;color:var(--heading)}
.post{position:absolute;left:375px;width:516px}
.avatar{position:absolute;left:0;top:0;width:78px;height:85px}
.post .copy{position:absolute;left:96px;top:14px;width:420px}
.post .more{position:absolute;right:2px;top:43px}
.byline{position:absolute;left:96px;top:56px;font-size:11px;font-weight:700;line-height:13px;letter-spacing:.8px}
.dots{left:375px;top:1076px;width:516px;border-top:1px dotted var(--rule)}
.find{left:848px;top:1198px;font-family:"Jost",sans-serif;font-size:18px;color:#333}
.social{position:absolute;top:1230px;width:48px;height:48px;border-radius:7px;background:linear-gradient(180deg,#6e9fd2,#2c64a4)}
.footer{position:absolute;left:0;top:1311px;width:1263px;text-align:center;font-size:11px;font-weight:700;color:#222;letter-spacing:.6px}
</style>
</head>
<body>
<div class="stage">
  <div class="page">
    <div class="abs aqua-strip"></div>
    <div class="abs hero" role="img" aria-label="Abstract blue light swirl"></div>
    <div class="abs logo-column"><div class="name">VantaLume</div></div>
    <div class="abs nav-bar"></div>
    <nav class="abs nav">
      <span>HOME</span><span class="sep">|</span><span>ABOUT US</span><span class="sep">|</span><span>OUR SERVICES</span><span class="sep">|</span><span>OUR BLOG</span><span class="sep">|</span><span>CONTACT US</span>
    </nav>
    <div class="abs hero-marks">???</div>
    <div class="abs tagline">What people are saying about<br>brands, products?</div>

    <div class="abs sidebar"></div>
    <svg class="abs wave" width="1003" height="220" viewBox="0 0 1003 220">
      <defs>
        <linearGradient id="waveFill" x1="0" y1="0" x2="0" y2="1">
          <stop offset="0" stop-color="#1f6fc0"/><stop offset="1" stop-color="#3a93e0"/>
        </linearGradient>
        <clipPath id="belowWave">
          <path d="M0 77 C200 70 400 100 560 140 C720 180 860 195 1003 192 L1003 220 L0 220 Z"/>
        </clipPath>
      </defs>
      <path d="M0 30 C200 10 400 40 600 80 C800 112 900 70 1003 52 L1003 220 L0 220 Z" fill="url(#waveFill)"/>
      <path d="M0 77 C200 70 400 100 560 140 C720 180 860 195 1003 192 L1003 220 L0 220 Z" fill="#fff"/>
      <rect x="60" y="60" width="280" height="160" fill="#ececec" clip-path="url(#belowWave)"/>
      <path d="M0 77 C200 70 400 100 560 140 C720 180 860 195 1003 192" fill="none" stroke="#7cc0f2" stroke-width="2"/>
      <path d="M0 30 C200 10 400 40 600 80 C800 112 900 70 1003 52" fill="none" stroke="#0d4f96" stroke-width="3"/>
    </svg>
    <div class="abs call">CLICK TO<br>CALL NOW</div>
    <svg class="abs call-icon" width="90" height="90" viewBox="0 0 90 90" role="img" aria-label="Phone icon">
      <circle cx="46" cy="47" r="38" fill="#f4f6f8" stroke="#c8d2dc" stroke-width="2"/>
      <rect x="34" y="24" width="24" height="46" rx="5" fill="#2e3238"/>
      <rect x="38" y="29" width="16" height="12" fill="#cfd6dc"/>
      <g fill="#cfd6dc">
        <rect x="38" y="45" width="4" height="3"/><rect x="44" y="45" width="4" height="3"/><rect x="50" y="45" width="4" height="3"/>
        <rect x="38" y="51" width="4" height="3"/><rect x="44" y="51" width="4" height="3"/><rect x="50" y="51" width="4" height="3"/>
        <rect x="38" y="57" width="4" height="3"/><rect x="44" y="57" width="4" height="3"/><rect x="50" y="57" width="4" height="3"/>
      </g>
    </svg>

    <div class="panel search">
      <div class="panel-title">Search</div>
      <div class="field"></div>
      <svg class="abs" style="left:186px;top:40px" width="30" height="28" viewBox="0 0 30 28">
        <circle cx="12" cy="11" r="8" fill="#eef3f7" stroke="#666" stroke-width="2"/>
        <line x1="18" y1="17" x2="26" y2="25" stroke="#444" stroke-width="4" stroke-linecap="round"/>
      </svg>
    </div>

    <div class="panel cases">
      <div class="panel-title">Case Studies</div>
      <h4>TOPIC 1</h4>
      <p>Lorem Ipsum is simply dummy text of the printing and typesetting industry. Lorem Ipsum has been the industry's standard dummy text ever since the 1500s, when an unknown printer took a galley of type and scrambled it to make a type specimen book.</p>
      <div class="more">Read More</div>
    </div>

    <form class="panel contact">
      <div class="panel-title">Contact Form</div>
      <label style="top:53px">Name</label><div class="field" style="top:69px"></div>
      <label style="top:106px">Email</label><div class="field" style="top:121px"></div>
      <label style="top:159px">Subject</label><div class="field" style="top:176px"></div>
      <label style="top:211px">Comments</label><div class="field" style="top:229px;height:100px"></div>
      <div class="btn" style="left:30px">Submit</div>
      <div class="btn" style="left:120px">Clear</div>
    </form>

    <h1 class="abs main-title">WELCOME TO OUR WEBSITE</h1>
    <p class="abs copy intro">Lorem Ipsum is simply dummy text of the printing and typesetting industry. Lorem Ipsum has been the industry's standard dummy text ever since the 1500s, when an unknown printer took a galley of type and scrambled it to make a type specimen book. It has survived not only five centuries, but also the leap into electronic typesetting, remaining essentially unchanged. It was popularised in the 1960s with the release of Letraset sheets containing Lorem Ipsum passages, and more recently with desktop publishing software like Aldus PageMaker including versions of Lorem Ipsum.</p>
    <div class="abs photo team" role="img" aria-label="Photograph of a business team"></div>
    <p class="abs copy body-text">It is a long established fact that a reader will be distracted by the readable content of a page when looking at its layout. The point of using Lorem Ipsum is that it has a more-or-less normal distribution of letters, as opposed to using 'Content here, content here', making it look like readable English. Many desktop publishing packages and web page editors now use Lorem Ipsum as their default model text, and a search for 'lorem ipsum' will uncover many web sites still in their infancy. Various versions have evolved over the years, sometimes by accident, sometimes on purpose.</p>

    <h2 class="abs blog-title">LATEST BLOG POST:</h2>
    <article class="post" style="top:967px">
      <div class="avatar photo" role="img" aria-label="Portrait photo of the author" style="background:linear-gradient(180deg,#e9e6e2,#c9b8a6 60%,#f3f3f3)"></div>
      <p class="copy">It is a long established fact that a reader will be distracted by the readable content of a page when looking at its layout.</p>
      <div class="more">Read More</div>
      <div class="byline">By: Ravi O.<br>05-05-2010</div>
    </article>
    <div class="abs dots"></div>
    <article class="post" style="top:1106px">
      <div class="avatar photo" role="img" aria-label="Portrait photo of the author" style="background:linear-gradient(180deg,#3c5e6c,#b89580 55%,#5d6f78)"></div>
      <p class="copy">It is a long established fact that a reader will be distracted by the readable content of a page when looking at its layout.</p>
      <div class="more">Read More</div>
      <div class="byline">By: Lena Marsh<br>03-05-2010</div>
    </article>

    <div class="abs find">FIND US ON</div>
    <div class="social" style="left:810px" role="img" aria-label="Social link"></div>
    <div class="social" style="left:873px" role="img" aria-label="Social link"></div>
    <div class="social" style="left:936px" role="img" aria-label="Feed link"></div>
  </div>
  <div class="footer">Copyright © 2008 vantalume.example</div>
</div>
</body>
</html>
```